Hadley's Groundwork Crew needs a logo/business cards.

i've just started a new Labouring Business, Called Hadley's Groundwork Crew, I provide high quality labouring servicing to local Builders and Tradesmen.
I'd like my business cards to reflect the hard work and dedication I put into my business.
I'd like to see Burnt Orange and blacks in the cards and logo.
I want my cards to catch peoples eye as there is A lot of dull business cards in my industry.

Target Market(s)

Builders and other tradesmen

Contact Information for Business Card

Hadley's Groundwork Crew

Font styles to use
Sans Serif

Colors
f78f20
ffc214
000000
ffffff

Requirements
Must have
• My name : Tom Hadley
• My Number: 0457962381
• Email Address : hadleygroundworkcrew@mailbarn.net
• A Sharp and Professional Design
Nice to have
• A unique design that separates my Cards from others,
• As I try to provide unique service to my clients I'd love my cards/logo to reflect this.

```html
<!DOCTYPE html>
<html lang="en">
<head>
<meta charset="utf-8">
<title>Hadley's Groundwork Crew – Business Card</title>
<link href="https://fonts.googleapis.com/css2?family=Lato:wght@400;700&display=swap" rel="stylesheet">
<style>
  :root {
    --bg: #2b2b2d;
    --card: #1c1d1f;
    --card-back: #161719;
    --pattern-light: #2a2b2e;
    --orange: #f78f20;
    --white: #ffffff;
    --grey: #d4d4d4;
    --rule: #4a4a4d;
  }
  html, body {
    margin: 0;
    padding: 0;
    width: 1200px;
    height: 1108px;
    overflow: hidden;
    background: var(--bg);
    font-family: "Lato", sans-serif;
  }
  .canvas {
    position: relative;
    width: 1200px;
    height: 1108px;
  }
  .card {
    position: absolute;
    top: 174px;
    width: 460px;
    height: 760px;
    border-radius: 24px;
    box-shadow: 0 18px 40px rgba(0,0,0,0.45);
    overflow: hidden;
  }
  .card--front { left: 110px; background: var(--card); }
  .card--back  { left: 630px; background: var(--card-back); }

  .brand {
    position: absolute;
    top: 150px;
    left: 0;
    right: 0;
    display: flex;
    flex-direction: column;
    align-items: center;
  }
  .brand__mark {
    width: 140px;
    height: 140px;
    border-radius: 50%;
    background: var(--orange);
  }
  .brand__name {
    margin-top: 22px;
    font-weight: 700;
    color: var(--orange);
    text-align: center;
    text-transform: uppercase;
  }
  .brand__name-main {
    display: block;
    font-size: 46px;
    line-height: 1;
    letter-spacing: 0.5px;
  }
  .brand__name-sub {
    display: block;
    margin-top: 8px;
    font-size: 15px;
    letter-spacing: 5px;
  }

  .contact {
    position: absolute;
    top: 500px;
    left: 0;
    right: 0;
    text-align: center;
  }
  .contact__name {
    font-weight: 700;
    font-size: 32px;
    color: var(--orange);
    letter-spacing: 0.3px;
  }
  .contact__rule {
    width: 150px;
    height: 1px;
    margin: 14px auto;
    background: var(--rule);
  }
  .contact__line {
    font-weight: 400;
    font-size: 19px;
    line-height: 1.45;
    color: var(--grey);
  }

  .back__pattern {
    position: absolute;
    inset: 0;
    background:
      radial-gradient(ellipse at 60% 25%, var(--pattern-light) 0%, rgba(42,43,46,0) 65%),
      linear-gradient(170deg, #222326 0%, var(--card-back) 80%);
  }
  .back__mark {
    position: absolute;
    left: 0;
    right: 0;
    bottom: 118px;
    text-align: center;
    font-weight: 700;
    font-size: 18px;
    letter-spacing: 3px;
    color: var(--white);
    text-transform: uppercase;
  }
</style>
</head>
<body>
  <div class="canvas">
    <section class="card card--front">
      <div class="brand">
        <div class="brand__mark"></div>
        <div class="brand__name">
          <span class="brand__name-main">Hadley's</span>
          <span class="brand__name-sub">Groundwork Crew</span>
        </div>
      </div>
      <div class="contact">
        <div class="contact__name">TOM HADLEY</div>
        <div class="contact__rule"></div>
        <div class="contact__line">0457962381</div>
        <div class="contact__line">hadleygroundworkcrew@mailbarn.net</div>
      </div>
    </section>

    <section class="card card--back">
      <div class="back__pattern" role="img" aria-label="Tone-on-tone repeating brand pattern across the card back"></div>
      <div class="back__mark">Hadley's</div>
    </section>
  </div>
</body>
</html>
```